Harborline Motors LLC

Car Dealer Customer Service
Address: 2741 Linden Avenue, Shelbyville, TN 37162
web: www.harborlinemotorstn.net
email: harborlinemotorstn@mailbox-example.net
Phone: (931) 555-0148
Phone: (629) 555-0173

```html
<!DOCTYPE html>
<html lang="en">
<head>
<meta charset="utf-8">
<title>Harborline Motors LLC — Business Card</title>
<link rel="stylesheet" href="https://fonts.googleapis.com/css2?family=Montserrat:wght@400;500;700&display=swap">
<style>
  :root {
    --backdrop: #3a3a3a;
    --card-white: #ffffff;
    --card-black: #171717;
    --brand-blue: #1f6fae;
    --edge-blue: #2a8fd6;
    --accent-gold: #eab040;
    --text-grey: #555555;
    --emboss-grey: #5b5b5b;
  }
  * { margin: 0; padding: 0; box-sizing: border-box; }
  html, body {
    width: 1200px; height: 801px; overflow: hidden;
    background: var(--backdrop);
    font-family: "Montserrat", sans-serif;
  }
  .card {
    position: absolute;
    width: 560px; height: 320px;
    border-radius: 2px;
    box-shadow: 0 18px 40px rgba(0,0,0,.45);
  }
  .card-front {
    left: 50px; top: 110px;
    background: var(--card-white);
    border-bottom: 3px solid var(--edge-blue);
  }
  .card-back {
    left: 590px; top: 370px;
    background: var(--card-black);
    border-bottom: 2px solid var(--edge-blue);
    display: flex; align-items: center; justify-content: center;
  }
  .brand-mark {
    position: absolute; left: 0; right: 0; top: 48px;
    display: flex; align-items: center; justify-content: center; gap: 10px;
  }
  .brand-dot {
    width: 16px; height: 16px; border-radius: 50%;
    background: var(--accent-gold);
  }
  .brand-name {
    font-weight: 700; font-size: 24px; letter-spacing: .5px;
    color: var(--brand-blue); text-transform: uppercase;
  }
  .tagline-row {
    position: absolute; left: 30px; right: 30px; top: 150px;
    display: flex; align-items: center; gap: 12px;
  }
  .tagline-rule { flex: 1; height: 1.5px; background: var(--accent-gold); }
  .tagline {
    font-weight: 700; font-size: 17px; color: var(--brand-blue);
    text-transform: uppercase; white-space: nowrap;
  }
  .contact-list {
    position: absolute; left: 40px; bottom: 40px;
    list-style: none; font-size: 12.5px; color: var(--text-grey);
    line-height: 1.65;
  }
  .contact-list li { display: flex; align-items: center; gap: 8px; }
  .contact-list svg { width: 11px; height: 11px; fill: var(--brand-blue); flex: none; }
  .address-block {
    position: absolute; right: 30px; bottom: 40px;
    text-align: right; font-size: 12.5px; color: var(--text-grey);
    line-height: 1.65;
  }
  .address-block .web { color: var(--brand-blue); font-weight: 500; }
  .back-mark { display: flex; align-items: center; gap: 14px; }
  .back-mark .brand-dot { width: 22px; height: 22px; background: var(--emboss-grey); }
  .back-name {
    font-weight: 700; font-size: 32px; letter-spacing: 1px;
    color: var(--emboss-grey); text-transform: uppercase;
  }
</style>
</head>
<body>
  <section class="card card-front">
    <div class="brand-mark">
      <span class="brand-dot"></span>
      <span class="brand-name">Harborline Motors</span>
    </div>
    <div class="tagline-row">
      <span class="tagline-rule"></span>
      <span class="tagline">Car Dealer Customer Service</span>
      <span class="tagline-rule"></span>
    </div>
    <ul class="contact-list">
      <li><svg viewBox="0 0 24 24"><path d="M6.6 10.8a15 15 0 0 0 6.6 6.6l2.2-2.2a1 1 0 0 1 1-.25 11.4 11.4 0 0 0 3.6.57 1 1 0 0 1 1 1V20a1 1 0 0 1-1 1A17 17 0 0 1 3 4a1 1 0 0 1 1-1h3.5a1 1 0 0 1 1 1c0 1.25.2 2.45.57 3.57a1 1 0 0 1-.25 1z"/></svg>(931) 555-0148</li>
      <li><svg viewBox="0 0 24 24"><path d="M6.6 10.8a15 15 0 0 0 6.6 6.6l2.2-2.2a1 1 0 0 1 1-.25 11.4 11.4 0 0 0 3.6.57 1 1 0 0 1 1 1V20a1 1 0 0 1-1 1A17 17 0 0 1 3 4a1 1 0 0 1 1-1h3.5a1 1 0 0 1 1 1c0 1.25.2 2.45.57 3.57a1 1 0 0 1-.25 1z"/></svg>(629) 555-0173</li>
      <li><svg viewBox="0 0 24 24"><path d="M2 5h20v14H2zm2 2v.5l8 5 8-5V7z"/></svg>harborlinemotorstn@mailbox-example.net</li>
    </ul>
    <div class="address-block">
      <p>2741 Linden Avenue</p>
      <p>Shelbyville, TN 37162</p>
      <p class="web">www.harborlinemotorstn.net</p>
    </div>
  </section>

  <section class="card card-back">
    <div class="back-mark">
      <span class="brand-dot"></span>
      <span class="back-name">Harborline Motors</span>
    </div>
  </section>
</body>
</html>
```